massage therapy Business Card Design

massage therapy business card
I would like a custom logo created as well.
My vision is angel wings with the HB business initials in between them.
A very simple design.
Colors preferred are light blues and greens.

Target Market(s)

Massage, Spa, fitness

Industry/Entity Type

Massage Therapy

Contact Information for Business Card

A Harbor Breeze
Nora Campe
Massage Therapist and Veldane Pulse Method Practitioner
2870 Marlow Ridge Road, Conway, AR 72039
501-384-6190
nora.harborbreeze@mailvinto.com

Colors
abd036
33a6d7
3176b5
0255a3
0392cd
9bcb3c
cadf82

Requirements
Must have
• the logo must have angel wing.

```html
<!DOCTYPE html>
<html lang="en">
<head>
<meta charset="utf-8">
<title>A Harbor Breeze – Business Card</title>
<link rel="stylesheet" href="https://fonts.googleapis.com/css2?family=Open+Sans:ital,wght@0,400;0,600;0,700;1,400&display=swap">
<style>
  :root {
    --paper: #ffffff;
    --meadow-light: #f4f9e8;
    --meadow: #cfe39a;
    --sky-top: #ffffff;
    --sky: #0392cd;
    --navy: #0255a3;
    --leaf-light: #cadf82;
    --ink: #1d1d1b;
  }
  * { margin: 0; padding: 0; box-sizing: border-box; }
  html, body {
    width: 1200px;
    height: 704px;
    overflow: hidden;
    background: var(--paper);
  }
  .card {
    position: relative;
    width: 1200px;
    height: 704px;
    background: var(--paper);
    font-family: "Open Sans", Arial, sans-serif;
    color: var(--ink);
  }
  .card__meadow {
    position: absolute;
    left: 46px;
    top: 308px;
    width: 1107px;
    height: 348px;
    background: linear-gradient(to bottom, var(--paper) 0%, var(--meadow-light) 22%, var(--meadow) 100%);
  }
  .brand__mark {
    position: absolute;
    left: 346px;
    top: 50px;
    width: 513px;
    height: 254px;
    border-radius: 0 0 22px 22px;
    background: linear-gradient(to bottom, var(--sky-top) 0%, #9fd3ec 40%, var(--sky) 100%);
  }
  .brand__banner {
    position: absolute;
    left: 346px;
    top: 321px;
    width: 513px;
    height: 61px;
    border-radius: 14px;
    background: var(--navy);
    text-align: center;
  }
  .brand__name {
    font-size: 46px;
    font-weight: 600;
    line-height: 63px;
    letter-spacing: 0.3px;
    color: var(--leaf-light);
    text-transform: uppercase;
    white-space: nowrap;
  }
  .details {
    position: absolute;
    left: 46px;
    top: 409px;
    width: 1107px;
    text-align: center;
  }
  .details__name {
    font-size: 50px;
    font-weight: 700;
    line-height: 1;
    letter-spacing: 0.5px;
    text-transform: uppercase;
  }
  .details__role {
    margin-top: 28px;
    font-size: 30px;
    font-style: italic;
    line-height: 1;
  }
  .details__contact {
    margin-top: 46px;
    font-size: 30px;
    line-height: 1;
    white-space: nowrap;
  }
  .details__email {
    margin-top: 15px;
    font-size: 30px;
    line-height: 1;
  }
</style>
</head>
<body>
  <div class="card">
    <div class="card__meadow"></div>

    <div class="brand__mark" role="img" aria-label="Logo area: white angel wings on a sky blue panel"></div>
    <div class="brand__banner">
      <p class="brand__name">A Harbor Breeze</p>
    </div>

    <div class="details">
      <h1 class="details__name">Nora Campe</h1>
      <p class="details__role">Massage Therapist and Veldane Pulse Method Practitioner</p>
      <p class="details__contact">2870 Marlow Ridge Road, Conway, AR 72039 501-384-6190</p>
      <p class="details__email">nora.harborbreeze@mailvinto.com</p>
    </div>
  </div>
</body>
</html>
```